Phone Repair Business Card

I need a business card for my mobile phone/ smart phone and tablet repair business based in New Zealand. My business name is "T.K. Repairs". I would like to see a designer make a modern phone related business card, which could incorporate something to do with the Zorvel Kavlo as this is our main repaired product. i like the dark Grey and lime green colours

```html
<!DOCTYPE html>
<html lang="en">
<head>
<meta charset="utf-8">
<title>T.K. Repairs – Business Card</title>
<link rel="stylesheet" href="https://fonts.googleapis.com/css2?family=Marcellus&family=Overlock:wght@700&display=swap">
<style>
  :root {
    --card-bg: #111111;
    --lime: #8dc63f;
    --ghost-type: #1d1d1d;
    --mark-grey: #5a5a5a;
    --service-grey: #cfcfcf;
    --contact-white: #ffffff;
  }
  html, body {
    margin: 0;
    padding: 0;
    overflow: hidden;
    background: var(--card-bg);
  }
  .card {
    position: relative;
    width: 1200px;
    height: 667px;
    overflow: hidden;
    background: var(--card-bg);
    font-family: "Marcellus", serif;
  }
  .side-tab {
    position: absolute;
    background: var(--lime);
  }
  .side-tab--left {
    left: 0;
    top: 34px;
    width: 54px;
    height: 604px;
    border-radius: 0 44px 44px 0;
  }
  .side-tab--right {
    right: 0;
    top: 50px;
    width: 18px;
    height: 578px;
    border-radius: 22px 0 0 22px;
  }
  .ghost-word {
    position: absolute;
    left: 108px;
    top: -42px;
    margin: 0;
    font-size: 158px;
    letter-spacing: 0.42em;
    color: var(--ghost-type);
    line-height: 1;
    white-space: nowrap;
  }
  .device-photo {
    position: absolute;
    left: 54px;
    top: 320px;
    width: 600px;
    height: 347px;
  }
  .brand-name {
    position: absolute;
    left: 292px;
    top: 250px;
    margin: 0;
    font-size: 170px;
    line-height: 1;
    color: var(--mark-grey);
    letter-spacing: -0.02em;
  }
  .details {
    position: absolute;
    left: 619px;
    top: 216px;
    width: 560px;
  }
  .details__title {
    margin: 0 0 27px;
    font-size: 38px;
    font-weight: 400;
    letter-spacing: 0.2em;
    color: var(--lime);
    line-height: 1;
  }
  .details__services {
    margin: 0 0 16px;
    font-size: 29px;
    line-height: 45px;
    color: var(--service-grey);
  }
  .contact-list {
    margin: 0;
    padding: 0;
    list-style: none;
    font-family: "Overlock", sans-serif;
    font-weight: 700;
    font-size: 27px;
    line-height: 36px;
  }
  .contact-list__label {
    color: var(--lime);
  }
  .contact-list__value {
    color: var(--contact-white);
  }
</style>
</head>
<body>
  <main class="card">
    <div class="side-tab side-tab--left"></div>
    <div class="side-tab side-tab--right"></div>

    <p class="ghost-word" aria-hidden="true">REPAIRS</p>

    <svg class="device-photo" role="img" aria-label="Photo of the back of a black Kavlo smartphone with the Zorvel emblem, lying at an angle" viewBox="0 0 600 347">
      <defs>
        <linearGradient id="device-shade" x1="0" y1="0" x2="1" y2="1">
          <stop offset="0" stop-color="#1a1a1a"/>
          <stop offset="0.6" stop-color="#0c0c0c"/>
          <stop offset="1" stop-color="#2a2a2a"/>
        </linearGradient>
      </defs>
      <path d="M0 20 L420 60 Q460 64 480 100 L580 300 L600 347 L0 347 Z" fill="url(#device-shade)"/>
    </svg>

    <p class="brand-name">T.K.</p>

    <section class="details">
      <h1 class="details__title">REPAIRS</h1>
      <p class="details__services">MOBILE PHONE /&nbsp; SMART PHONE &amp;<br>TABLET REPAIR</p>
      <ul class="contact-list">
        <li><span class="contact-list__label">E-mail &nbsp;: </span> <span class="contact-list__value">yourname@yourdomain.com</span></li>
        <li><span class="contact-list__label">Contact &nbsp;: </span> <span class="contact-list__value">+00 000 000000</span></li>
        <li><span class="contact-list__label">Web &nbsp;: </span><span class="contact-list__value">www.yoursite.com</span></li>
      </ul>
    </section>
  </main>
</body>
</html>
```